Creative Bright Solar, Geothermal and Wind Website! GO GREEN

We are looking to reface our website. Brightfield energy partners of NY, LLC does Solar, Geothermal and Wind systems. Both on grid and off grid.
Im looking for a fun simple and informative website for customers to sign up for free quotes and see all our systems on a pin point map.
Solar is our main focus and we provide zero down financing with low monthly payments.

Main page should have three buttons to choose solar geo or wind.
"Get a FREE quote" visible and a spot to fill in name, phone, address, email and check boxes for solar geo and wind.

A map of New York that will include all of our systems we have done with a box stating the system size and link to a page with pictures and details of the system.

A meet the team drop down with bios on company employees.

Our current website : bfepofny.com

WE DONT WANT ANYTHING like it. Please. We need simple, fun, up to date, creative an colorful.

Thank you

Target Market(s)

Residential home owners, Commercial and Agricultural

Industry/Entity Type

Solar

Number of Pages Required

2 page

Requirements
Must have
• Map to show all projects completed
• 3 buttons Solar, Geothermal and Wind
• zero down financing
• Low monthly payments
• *** The ability to run the platform Joomla template on the web design.
Nice to have
• I added some pics, please use if you feel fit. your choice.
Should not have
• White background

```html
<!DOCTYPE html>
<html lang="en">
<head>
<meta charset="utf-8">
<title>Brightfield Energy Partners of NY</title>
<link href="https://fonts.googleapis.com/css2?family=Open+Sans:wght@400;600;700;800&display=swap" rel="stylesheet">
<style>
:root{
  --green:#3f9a2c;
  --green-dark:#2f7d22;
  --green-light:#6cbf3a;
  --footer:#2b7f2a;
  --footer-dark:#1f5e1f;
  --tan:#efe4cd;
  --ink:#3b3b3b;
  --muted:#7a7a7a;
  --line:#e2dccf;
  --blue:#3c7fc2;
}
*{box-sizing:border-box;margin:0;padding:0}
html,body{width:1200px;height:2332px;overflow:hidden}
body{font-family:"Open Sans",Arial,sans-serif;color:var(--ink);background:var(--tan)}
.page{width:1200px;height:2332px;position:relative;background:linear-gradient(#f4ead6 0,#efe4cd 630px,#f6f1e6 630px)}

/* header */
.site-header{height:150px;padding:28px 55px 0;display:flex;justify-content:space-between}
.brand{display:flex;align-items:center;gap:14px}
.brand-mark{width:58px;height:58px;border-radius:50%;background:#f1c232}
.brand-name{font-weight:700;font-size:17px;color:var(--green-dark);line-height:1.25;width:200px}
.brand-phone{display:block;color:#d23a2a;font-size:16px}
.header-right{text-align:right}
.call{font-size:15px;color:var(--muted);display:flex;align-items:center;justify-content:flex-end;gap:8px}
.call b{color:var(--green);font-size:17px}
.main-nav{margin-top:22px;display:flex;gap:30px;font-size:15px;font-weight:600}
.main-nav a{color:#555;text-decoration:none}
.main-nav a.active{color:var(--green)}

/* hero */
.hero{position:absolute;top:196px;left:55px;width:1090px;height:400px;display:flex;box-shadow:0 2px 6px rgba(0,0,0,.15)}
.hero-photo{flex:1;background:linear-gradient(180deg,#9fc2e6 0%,#d7e6f2 45%,#6f8296 62%,#3d4d63 100%);position:relative}
.dots{position:absolute;bottom:14px;left:50%;display:flex;gap:7px}
.dots i{width:10px;height:10px;border-radius:50%;background:#fff;opacity:.6}
.dots i:first-child{opacity:1}
.quote-box{width:300px;background:var(--green-light);padding:26px 24px;color:#fff}
.quote-box h2{font-size:20px;font-weight:600;line-height:1.15}
.quote-box h2 span{display:block;font-size:30px;font-weight:800}
.field{height:32px;background:#fff;border-radius:2px;margin-top:12px;font-size:13px;color:#999;padding:7px 10px}
.checks{display:flex;gap:10px;margin-top:14px;font-size:13px;align-items:center}
.checks i{display:inline-block;width:13px;height:13px;background:#fff;vertical-align:-2px;margin-right:4px}
.submit{margin-left:auto;background:var(--green-dark);padding:6px 12px;font-weight:700}

/* choice buttons */
.choices{position:absolute;top:646px;left:55px;width:1090px;height:66px;display:flex;gap:12px}
.choice{flex:1;background:#fff;border:1px solid var(--line);display:flex;align-items:center;justify-content:center;gap:14px;font-weight:700;font-size:17px;text-transform:uppercase;color:#444;border-bottom:4px solid var(--green)}
.choice .ico{width:38px;height:38px;border-radius:50%;display:flex;align-items:center;justify-content:center}
.choice.team{background:var(--green);color:#fff;border-color:var(--green-dark)}

/* welcome */
.section-title{font-size:20px;font-weight:700;color:#444}
.welcome{position:absolute;top:745px;left:55px;width:1090px}
.welcome-body{display:flex;gap:26px;margin-top:18px}
.welcome-photo{width:380px;height:180px;flex:none;background:linear-gradient(180deg,#b9d4ec 0%,#cfdcc0 45%,#4a6a8a 70%,#2f3f58 100%)}
.welcome p{flex:1;font-size:13px;line-height:1.55;color:var(--muted)}

/* finance */
.finance{position:absolute;top:1045px;left:55px;width:1090px;display:flex;gap:30px}
.finance-col{flex:1;background:#fff;border-top:3px solid var(--green);padding:22px 24px;height:292px}
.finance h3{font-size:19px;font-weight:700;color:#444;margin-bottom:12px}
.finance p{font-size:13px;line-height:1.55;color:var(--muted)}
.finance-top{display:flex;gap:18px;margin-bottom:12px}
.team-photo{width:200px;height:120px;flex:none;background:linear-gradient(180deg,#9cc3e8,#7ca764 60%,#4f7f3d)}
.ticks{list-style:none;margin-top:10px}
.ticks li{font-size:13px;color:var(--muted);padding:5px 0;display:flex;align-items:center;gap:10px}

/* projects */
.projects{position:absolute;top:1440px;left:55px;width:1090px;text-align:center}
.projects h2{font-size:22px;font-weight:700;color:var(--green)}
.map{margin:22px auto 0;width:1090px;height:290px;background:linear-gradient(180deg,#8fc86b 0%,#5da742 55%,#3d8a2d 100%);clip-path:polygon(9% 0,91% 0,100% 100%,0 100%)}
.project-list{display:flex;gap:20px;margin-top:28px;text-align:left}
.project-col{flex:1;border-top:2px solid var(--green);padding-top:10px}
.project-col li{list-style:none;font-size:12px;color:var(--muted);line-height:1.9}

/* footer */
.site-footer{position:absolute;top:2020px;left:0;width:1200px;height:252px;background:var(--footer);color:#e8f4e4;padding:34px 55px;display:flex;gap:40px}
.foot-col{flex:1}
.foot-col h4{font-size:15px;font-weight:700;color:#fff;text-transform:uppercase;margin-bottom:14px}
.foot-col ul{list-style:none}
.foot-col li{font-size:12.5px;line-height:2;display:flex;align-items:center;gap:8px}
.post{display:flex;gap:10px;font-size:12px;line-height:1.45;margin-bottom:12px}
.post .mark{width:16px;height:16px;flex:none;background:#cfe9c6;border-radius:3px;margin-top:2px}
.post a{color:#bfe3b1}
.contact-line{font-size:12.5px;line-height:1.7;display:flex;gap:8px;align-items:flex-start;margin-bottom:8px}
.contact-line.big{font-size:22px;font-weight:700;color:#fff;align-items:center}
.social-dot{width:14px;height:14px;border-radius:50%;background:#cfe9c6}
.copyright{position:absolute;top:2272px;left:0;width:1200px;height:60px;background:var(--footer-dark);color:#bcd9b5;font-size:12px;text-align:center;line-height:60px;letter-spacing:.5px}
</style>
</head>
<body>
<div class="page">

  <header class="site-header">
    <div class="brand">
      <div class="brand-mark"></div>
      <div class="brand-name">Brightfield energy partners of NY, LLC <span class="brand-phone">315-555-0142</span></div>
    </div>
    <div class="header-right">
      <div class="call">
        <svg width="16" height="16" viewBox="0 0 24 24"><path fill="#3f9a2c" d="M6.6 10.8a15.5 15.5 0 0 0 6.6 6.6l2.2-2.2a1 1 0 0 1 1-.25 11.4 11.4 0 0 0 3.6.57 1 1 0 0 1 1 1V20a1 1 0 0 1-1 1A17 17 0 0 1 3 4a1 1 0 0 1 1-1h3.5a1 1 0 0 1 1 1c0 1.25.2 2.45.57 3.6a1 1 0 0 1-.25 1z"/></svg>
        Call us : <b>315-555-0142</b>
      </div>
      <nav class="main-nav">
        <a class="active" href="#">Home</a><a href="#">Solar Power</a><a href="#">Wind Power</a><a href="#">Installations</a><a href="#">Contact Us</a>
      </nav>
    </div>
  </header>

  <section class="hero">
    <div class="hero-photo" role="img" aria-label="Wind turbines and rows of solar panels under a bright sky">
      <div class="dots"><i></i><i></i><i></i></div>
    </div>
    <form class="quote-box">
      <h2>Get the free <span>QUOTES NOW!</span></h2>
      <div class="field">Name</div>
      <div class="field">Phone</div>
      <div class="field">Address</div>
      <div class="field">Email</div>
      <div class="checks"><span><i></i>Solar</span><span><i></i>Geo</span><span><i></i>Wind</span><span class="submit">Submit</span></div>
    </form>
  </section>

  <nav class="choices">
    <a class="choice"><span class="ico" style="background:#f3c43a"><svg width="22" height="22" viewBox="0 0 24 24"><circle cx="12" cy="12" r="5" fill="#fff"/></svg></span>Solar</a>
    <a class="choice"><span class="ico" style="background:var(--green)"><svg width="22" height="22" viewBox="0 0 24 24"><path d="M12 4v16M6 10h12" stroke="#fff" stroke-width="3"/></svg></span>Geothermal</a>
    <a class="choice"><span class="ico" style="background:var(--blue)"><svg width="22" height="22" viewBox="0 0 24 24"><path d="M12 12l0-8M12 12l7 4M12 12l-7 4M12 12v9" stroke="#fff" stroke-width="2.5" stroke-linecap="round"/></svg></span>Wind</a>
    <a class="choice team">Meet Our Team <svg width="18" height="18" viewBox="0 0 24 24"><path d="M9 5l7 7-7 7" stroke="#fff" stroke-width="3" fill="none"/></svg></a>
  </nav>

  <section class="welcome">
    <h2 class="section-title">Welcome To Our Website</h2>
    <div class="welcome-body">
      <div class="welcome-photo" role="img" aria-label="Field of solar panels on a clear day"></div>
      <p>We install solar, geothermal and wind systems that help homes, farms and businesses across New York lower their energy bills. Every system is designed around your site, your usage and your goals, whether you want to stay on the grid or go fully off grid. Our crews handle everything from the first visit to final hookup, so the switch to clean power is simple. Solar is our main focus, and we offer options that make it easy to start today with no money down. Take a look at our recent projects, request a free quote in minutes, and see how much you could save each month while doing your part for a greener state.</p>
    </div>
  </section>

  <section class="finance">
    <div class="finance-col">
      <h3>Zero down financing</h3>
      <div class="finance-top">
        <p>Go solar without a large upfront cost. Our zero down plans let you start producing your own clean power right away while you pay over time.</p>
        <div class="team-photo" role="img" aria-label="Installation crew standing beside a solar array"></div>
      </div>
      <p>Solar power is one of the smartest home upgrades you can make. We work with trusted lenders to find a plan that fits your budget, so you can cut your electric bill, protect against rising rates and raise the value of your property from day one.</p>
    </div>
    <div class="finance-col">
      <h3>Low monthly payments</h3>
      <p>Keep more money in your pocket. In many cases your monthly payment is lower than the electric bill it replaces.</p>
      <ul class="ticks">
        <li><svg width="14" height="14" viewBox="0 0 24 24"><path d="M4 12l5 5 11-11" stroke="#3f9a2c" stroke-width="3" fill="none"/></svg>Payments as low as your bill</li>
        <li><svg width="14" height="14" viewBox="0 0 24 24"><path d="M4 12l5 5 11-11" stroke="#3f9a2c" stroke-width="3" fill="none"/></svg>Fixed rates and clear terms</li>
        <li><svg width="14" height="14" viewBox="0 0 24 24"><path d="M4 12l5 5 11-11" stroke="#3f9a2c" stroke-width="3" fill="none"/></svg>Quick and easy approval</li>
        <li><svg width="14" height="14" viewBox="0 0 24 24"><path d="M4 12l5 5 11-11" stroke="#3f9a2c" stroke-width="3" fill="none"/></svg>Incentives applied for you</li>
        <li><svg width="14" height="14" viewBox="0 0 24 24"><path d="M4 12l5 5 11-11" stroke="#3f9a2c" stroke-width="3" fill="none"/></svg>Savings from the first month</li>
        <li><svg width="14" height="14" viewBox="0 0 24 24"><path d="M4 12l5 5 11-11" stroke="#3f9a2c" stroke-width="3" fill="none"/></svg>Local service and support</li>
      </ul>
    </div>
  </section>

  <section class="projects">
    <h2>Recent Solar Power Projects</h2>
    <div class="map" role="img" aria-label="Map of New York State with pins marking completed solar, geothermal and wind projects"></div>
    <div class="project-list">
      <ul class="project-col"><li>Hillside Farm PV - Nedrow, NY</li><li>Maple Lane PV - Ithaca, NY</li><li>Orchard Barn Solar - Auburn, NY</li><li>Creekside PV - Oswego, NY</li><li>Stone Mill Solar - Cortland, NY</li></ul>
      <ul class="project-col"><li>Lakeview Solar Heating - Watertown, NY</li><li>Pine Ridge Geo Heating - Rome, NY</li><li>Valley Geo Heating - Utica, NY</li><li>Meadow Geo System - Oneida, NY</li><li>Brookside Geo Heating - Fulton, NY</li></ul>
      <ul class="project-col"><li>Grand Oak PV - Syracuse, NY</li><li>Riverbend Solar - Baldwinsville, NY</li><li>Westfield PV Array - Camillus, NY</li><li>Sunrise Dairy PV - Skaneateles, NY</li><li>Cedar Hill Solar - Geneva, NY</li></ul>
      <ul class="project-col"><li>North Wind Turbine - Lowville, NY</li><li>Ridge Top Wind - Boonville, NY</li><li>Prairie Wind - Malone, NY</li><li>Hilltop Wind Farm - Canton, NY</li><li>Summit Wind - Potsdam, NY</li></ul>
    </div>
  </section>

  <footer class="site-footer">
    <div class="foot-col">
      <h4>Links</h4>
      <ul><li>› Sitemap</li><li>› Installations</li><li>› News</li><li>› Our Partners</li></ul>
    </div>
    <div class="foot-col">
      <h4>Latest Posts</h4>
      <div class="post"><span class="mark"></span><p>Good morning! New panels went live today on a dairy farm near Auburn. <a href="#">bfepofny.com</a></p></div>
      <div class="post"><span class="mark"></span><p>Good morning! Ask us about zero down solar before rates go up again. <a href="#">bfepofny.com</a></p></div>
    </div>
    <div class="foot-col">
      <h4>Contact Us</h4>
      <div class="contact-line"><svg width="14" height="18" viewBox="0 0 24 30"><path d="M12 0a10 10 0 0 0-10 10c0 8 10 20 10 20s10-12 10-20A10 10 0 0 0 12 0zm0 14a4 4 0 1 1 0-8 4 4 0 0 1 0 8z" fill="#cfe9c6"/></svg>14 Linden Court<br>Maplebrook, NY 10999</div>
      <div class="contact-line big"><svg width="18" height="18" viewBox="0 0 24 24"><path fill="#fff" d="M6.6 10.8a15.5 15.5 0 0 0 6.6 6.6l2.2-2.2a1 1 0 0 1 1-.25 11.4 11.4 0 0 0 3.6.57 1 1 0 0 1 1 1V20a1 1 0 0 1-1 1A17 17 0 0 1 3 4a1 1 0 0 1 1-1h3.5a1 1 0 0 1 1 1c0 1.25.2 2.45.57 3.6a1 1 0 0 1-.25 1z"/></svg>315-555-0142</div>
      <div class="contact-line"><svg width="16" height="14" viewBox="0 0 24 18"><rect x="1" y="1" width="22" height="16" fill="none" stroke="#cfe9c6" stroke-width="2"/><path d="M1 1l11 9 11-9" fill="none" stroke="#cfe9c6" stroke-width="2"/></svg>info@bfepofny.com</div>
    </div>
    <div class="foot-col">
      <h4>Social Media</h4>
      <ul><li><span class="social-dot"></span>Community</li><li><span class="social-dot"></span>Updates</li><li><span class="social-dot"></span>Circles</li><li><span class="social-dot"></span>Videos</li></ul>
    </div>
  </footer>
  <div class="copyright">COPYRIGHT © 2015, BRIGHTFIELD ENERGY PARTNERS OF NY, LLC</div>

</div>
</body>
</html>
```